Loom Vane Wordpress Blog Page

Loom Vane is a supplier of custom printed clothing. Our E-Commerce platform uses a reverse proxy to incorporate a Wordpress Blog into the site.

E-Commerce site: http://www.loomvane.example

E-Commerce site incorporates blog page here: http://www.loomvane.example/blog

Currently running Wordpress Blog site: http://www.loomvane-journal.example

We need our blog styled to fit in with the look and feel of the website. The Header and Footer in particular are key to the blog appearing to the user as part of the site. Some key elements may not be possible such as the shopping cart, or other dynamic elements. The rest of the blog needs to be styled to fit in with the site as much as possible.

Font styles to use
Other font styles liked:
• Headline font is HWT ARTZ

Requirements
Must have
• Styled look and feel to fit in with current site design
• Must be responsive design and mobile friendly
• Must be SEO standards compliant

```html
<!DOCTYPE html>
<html lang="en">
<head>
<meta charset="utf-8">
<title>Loom Vane — Blog</title>
<link href="https://fonts.googleapis.com/css2?family=Open+Sans:wght@400;600;700;800&display=swap" rel="stylesheet">
<style>
:root{
  --blue:#1b9ad8;
  --blue-dark:#1284bd;
  --navy:#0c2a47;
  --navy-deep:#081e34;
  --ink:#2b2b2b;
  --muted:#8a8a8a;
  --line:#e3e3e3;
  --paper:#ffffff;
  --soft:#f3f5f7;
  --play-bg:rgba(8,30,52,.6);
}
*{box-sizing:border-box;margin:0;padding:0}
html,body{width:1200px;height:2772px;overflow:hidden}
body{position:relative;background:var(--paper);font-family:"Open Sans",Arial,sans-serif;color:var(--ink);font-size:12px;line-height:1.5}
a{color:inherit;text-decoration:none}
ul{list-style:none}

/* header + hero */
.hero{position:absolute;left:0;top:0;width:1200px;height:540px;background:linear-gradient(180deg,#1d5f9c 0%,#3b93d4 35%,#8cc6ee 70%,#d9ecf8 100%)}
.hero-photo{position:absolute;left:0;top:230px;width:1200px;height:310px;background:linear-gradient(180deg,rgba(255,255,255,0) 0%,rgba(200,170,150,.35) 60%,rgba(120,110,120,.45) 100%)}
.topbar{position:absolute;left:0;top:0;width:1200px;height:44px;background:rgba(8,30,52,.55)}
.brand{position:absolute;left:96px;top:14px;display:flex;align-items:center;gap:10px;color:#fff;font-weight:800;font-size:26px;letter-spacing:.5px}
.brand-dot{width:26px;height:26px;border-radius:50%;background:var(--blue)}
.topbar-tools{position:absolute;right:96px;top:10px;display:flex;align-items:center;gap:16px;color:#fff;font-size:11px}
.search{width:210px;height:24px;background:rgba(255,255,255,.18);border:1px solid rgba(255,255,255,.35);border-radius:2px;padding:0 8px;line-height:22px;color:#cfe3f3}
.help strong{font-size:15px;font-weight:700}
.mainnav{position:absolute;right:96px;top:66px;display:flex;gap:0}
.mainnav a{display:block;padding:0 16px;height:34px;line-height:34px;color:#fff;font-weight:700;font-size:12px;text-transform:uppercase}
.hero-title{position:absolute;left:0;top:140px;width:1200px;text-align:center;color:#fff;font-weight:800;font-size:58px;letter-spacing:1px;text-transform:uppercase}

/* section titles */
.sec-title{font-size:20px;font-weight:800;text-transform:uppercase;color:var(--ink);padding-bottom:10px;border-bottom:1px solid var(--line);position:relative}
.sec-title span{color:var(--blue)}
.sec-title::after{content:"";position:absolute;left:0;bottom:-1px;width:60px;height:3px;background:var(--blue)}

/* main column */
.main{position:absolute;left:96px;top:630px;width:700px}
.post-grid{display:grid;grid-template-columns:340px 340px;column-gap:20px;row-gap:26px;margin-top:26px}
.card-media{position:relative;height:200px;background:linear-gradient(135deg,#e8d3c0,#b98e74)}
.card-media.b{background:linear-gradient(135deg,#f0d9b5,#c78a5a)}
.card-media.c{background:linear-gradient(135deg,#7e6a63,#3c3036)}
.card-media.d{background:linear-gradient(135deg,#6c6e74,#2e2d33)}
.tag{position:absolute;left:0;bottom:0;background:var(--blue);color:#fff;font-size:9px;font-weight:700;text-transform:uppercase;padding:4px 12px}
.card-title{margin-top:12px;font-size:12px;font-weight:800;text-transform:uppercase;line-height:1.45}
.meta{color:var(--muted);font-size:9px;margin-top:6px}
.excerpt{color:#666;font-size:10.5px;margin-top:6px;line-height:1.6}
.btn{display:inline-block;background:var(--blue);color:#fff;font-size:10px;font-weight:700;text-transform:uppercase;padding:9px 18px;border-radius:2px}
.more{text-align:right;margin-top:24px}

.top-list{margin-top:44px}
.top-item{display:flex;gap:26px;height:216px;padding-top:22px}
.top-media{width:220px;height:160px;flex:none}
.tm1{background:linear-gradient(135deg,#d1b8a0,#6f5a50)}
.tm2{background:linear-gradient(180deg,#7ab4e6,#c8a56e)}
.tm3{background:linear-gradient(135deg,#b63a37,#e8dfd5)}
.top-item .card-title{margin-top:4px;font-size:12.5px}
.pager{display:flex;justify-content:center;gap:6px;margin-top:26px}
.pager a{display:block;min-width:26px;height:26px;line-height:24px;text-align:center;border:1px solid var(--line);font-size:10px;color:#555;padding:0 6px}
.pager a.on{background:var(--blue);border-color:var(--blue);color:#fff}

/* sidebar */
.side{position:absolute;left:840px;top:630px;width:264px}
.side p.lead{color:#777;font-size:10px;margin-top:14px}
.field{margin-top:10px;height:30px;border:1px solid var(--line);padding:0 10px;line-height:28px;color:#aaa;font-size:10px}
.side .btn{margin-top:10px}
.related{margin-top:34px}
.rel-item{display:flex;gap:12px;margin-top:16px;height:62px}
.rel-media{width:72px;height:58px;flex:none}
.r1{background:linear-gradient(135deg,#d7bca4,#7c5e4d)}
.r2{background:linear-gradient(135deg,#d8d0c8,#5a4b44)}
.r3{background:linear-gradient(135deg,#c9a37e,#6b4a37)}
.rel-item h4{font-size:10.5px;font-weight:800;text-transform:uppercase;line-height:1.4}
.side-more{text-align:center;margin-top:20px}
.ad{margin-top:30px;height:210px;background:linear-gradient(160deg,#1f1f24 0%,#3a3a42 55%,#d8b83a 100%)}
.videos{margin-top:24px}
.video{margin-top:18px;height:236px}
.video-media{position:relative;height:170px}
.v1{background:linear-gradient(135deg,#c9c9cc,#7d2a2a)}
.v2{background:linear-gradient(135deg,#7a9fcf,#d8c9b0)}
.v3{background:linear-gradient(135deg,#f2c16a,#a46a2a)}
.play{position:absolute;left:50%;top:50%;width:40px;height:40px;margin:-20px 0 0 -20px}
.video h4{margin-top:10px;font-size:10.5px;font-weight:800;text-transform:uppercase;line-height:1.4}

/* subscribe band */
.band{position:absolute;left:0;top:2328px;width:1200px;height:84px;background:var(--blue);color:#fff}
.band-inner{position:absolute;left:96px;top:27px;width:1008px;display:flex;align-items:center}
.band-inner svg{flex:none}
.band-inner p{margin-left:16px;font-size:15px;font-weight:600}
.band-form{margin-left:auto;display:flex}
.band-form .input{width:240px;height:32px;background:#fff;color:#aaa;font-size:10px;line-height:32px;padding:0 10px}
.band-form .go{height:32px;line-height:32px;background:var(--navy);color:#fff;font-weight:700;font-size:10px;padding:0 20px;text-transform:uppercase}

/* footer */
.footer{position:absolute;left:0;top:2412px;width:1200px;height:320px;background:var(--navy);color:#c9d6e3}
.foot-cols{position:absolute;left:96px;top:34px;width:1008px;display:grid;grid-template-columns:252px 252px 252px 252px}
.foot-cols h5{color:var(--blue);font-size:11px;font-weight:800;text-transform:uppercase;margin-bottom:12px}
.foot-cols li{font-size:10.5px;line-height:2.05}
.socials{display:flex;gap:12px;flex-wrap:wrap;width:120px}
.socials span{width:30px;height:30px;border-radius:50%;background:var(--blue);display:block}
.legal{position:absolute;left:0;top:2732px;width:1200px;height:40px;background:var(--navy-deep);color:#8ea3b8;font-size:9.5px}
.legal-inner{position:absolute;left:96px;top:13px;width:1008px;display:flex;align-items:center}
.cards{display:flex;gap:6px;margin-left:14px}
.cards span{width:30px;height:16px;background:#e8edf2;border-radius:2px;display:block}
.legal-inner .copy{margin-left:auto}
</style>
</head>
<body>

<header>
  <div class="hero">
    <div class="hero-photo" role="img" aria-label="Group of happy clients in printed tees leaping against a blue sky"></div>
  </div>
  <div class="topbar">
    <a class="brand" href="#"><span class="brand-dot"></span>Loom Vane</a>
    <div class="topbar-tools">
      <div class="search">Search</div>
      <a href="#">LOGIN</a>
      <a href="#">REGISTER</a>
      <span class="help">Need help? Call us <strong>1300 555 010</strong></span>
    </div>
  </div>
  <nav class="mainnav">
    <a href="#">Casual</a><a href="#">Work</a><a href="#">Active</a><a href="#">All Over</a><a href="#">Design Ideas</a><a href="#">Contact Us</a><a href="#">Get a Quote</a>
  </nav>
  <h1 class="hero-title">Comments of Happy Clients</h1>
</header>

<main class="main">
  <h2 class="sec-title">Blog <span>Posts</span></h2>
  <div class="post-grid">
    <article>
      <div class="card-media" role="img" aria-label="Woman wearing a printed summer top"><span class="tag">Fashion News</span></div>
      <h3 class="card-title">Lorem ipsum is simply dummy text<br>of the printing</h3>
      <p class="meta">12 March 2015</p>
      <p class="excerpt">Lorem ipsum is simply dummy text of the printing and type setting industry. Lorem the industry's...</p>
    </article>
    <article>
      <div class="card-media b" role="img" aria-label="Woman relaxing on the beach in a printed outfit"><span class="tag">Lifestyle</span></div>
      <h3 class="card-title">Lorem ipsum is simply dummy text<br>of the printing</h3>
      <p class="meta">12 March 2015</p>
      <p class="excerpt">Lorem ipsum is simply dummy text of the printing and type setting industry. Lorem the industry's...</p>
    </article>
    <article>
      <div class="card-media c" role="img" aria-label="Couple posing in matching printed jackets"><span class="tag">Style Guide</span></div>
      <h3 class="card-title">Lorem ipsum is simply dummy text<br>of the printing</h3>
      <p class="meta">12 March 2015</p>
      <p class="excerpt">Lorem ipsum is simply dummy text of the printing and type setting industry. Lorem the industry's...</p>
    </article>
    <article>
      <div class="card-media d" role="img" aria-label="Model in a dark printed active wear set"><span class="tag">Active Wear</span></div>
      <h3 class="card-title">Lorem ipsum is simply dummy text<br>of the printing</h3>
      <p class="meta">12 March 2015</p>
      <p class="excerpt">Lorem ipsum is simply dummy text of the printing and type setting industry. Lorem the industry's...</p>
    </article>
  </div>
  <div class="more"><a class="btn" href="#">View More Posts</a></div>

  <section class="top-list">
    <h2 class="sec-title">Top Most <span>Posts</span></h2>
    <article class="top-item">
      <div class="top-media tm1" role="img" aria-label="Athlete training in a printed gym shirt"></div>
      <div>
        <h3 class="card-title">Lorem ipsum is simply dummy text of the printing</h3>
        <p class="meta">12 March 2015</p>
        <p class="excerpt">Lorem ipsum is simply dummy text of the printing and typesetting industry. Lorem Ipsum has been the industry's standard dummy text ever since the 1500s, when an unknown printer took a galley of type and scrambled it to make a type specimen book. It has survived not only five centuries, but also the leap...</p>
      </div>
    </article>
    <article class="top-item">
      <div class="top-media tm2" role="img" aria-label="Runners in printed team tees on an outdoor track"></div>
      <div>
        <h3 class="card-title">Lorem ipsum is simply dummy text of the printing</h3>
        <p class="meta">12 March 2015</p>
        <p class="excerpt">Lorem ipsum is simply dummy text of the printing and typesetting industry. Lorem Ipsum has been the industry's standard dummy text ever since the 1500s, when an unknown printer took a galley of type and scrambled it to make a type specimen book. It has survived not only five centuries, but also the leap...</p>
      </div>
    </article>
    <article class="top-item">
      <div class="top-media tm3" role="img" aria-label="Sports team in red printed jerseys"></div>
      <div>
        <h3 class="card-title">Lorem ipsum is simply dummy text of the printing</h3>
        <p class="meta">12 March 2015</p>
        <p class="excerpt">Lorem ipsum is simply dummy text of the printing and typesetting industry. Lorem Ipsum has been the industry's standard dummy text ever since the 1500s, when an unknown printer took a galley of type and scrambled it to make a type specimen book. It has survived not only five centuries, but also the leap...</p>
      </div>
    </article>
    <nav class="pager">
      <a href="#">Prev</a><a class="on" href="#">1</a><a href="#">2</a><a href="#">3</a><a href="#">4</a><a href="#">5</a><a href="#">6</a><a href="#">7</a><a href="#">8</a><a href="#">…</a><a href="#">20</a><a href="#">Next</a>
    </nav>
  </section>
</main>

<aside class="side">
  <h2 class="sec-title">Newsletter <span>Signup</span></h2>
  <p class="lead">Get our latest updates through your email id</p>
  <div class="field">Enter your email id</div>
  <a class="btn" href="#">Subscribe Now</a>

  <section class="related">
    <h2 class="sec-title">Related <span>Posts</span></h2>
    <div class="rel-item"><div class="rel-media r1" role="img" aria-label="Woman in a printed tee"></div><h4>Lorem ipsum is simply dummy text</h4></div>
    <div class="rel-item"><div class="rel-media r2" role="img" aria-label="Man in a printed hoodie"></div><h4>Lorem ipsum is simply dummy text</h4></div>
    <div class="rel-item"><div class="rel-media r3" role="img" aria-label="Friends in printed shirts"></div><h4>Lorem ipsum is simply dummy text</h4></div>
    <div class="side-more"><a class="btn" href="#">View More Posts</a></div>
  </section>

  <div class="ad" role="img" aria-label="Sidebar advertisement banner"></div>

  <section class="videos">
    <h2 class="sec-title">Our <span>Videos</span></h2>
    <div class="video">
      <div class="video-media v1" role="img" aria-label="Video still of a printing workshop">
        <svg class="play" viewBox="0 0 40 40"><circle cx="20" cy="20" r="19" fill="var(--play-bg)" stroke="#fff" stroke-width="2"/><path d="M16 13 L27 20 L16 27 Z" fill="#fff"/></svg>
      </div>
      <h4>Lorem ipsum is simply dummy text of the printing</h4>
    </div>
    <div class="video">
      <div class="video-media v2" role="img" aria-label="Video still of a team wearing printed shirts">
        <svg class="play" viewBox="0 0 40 40"><circle cx="20" cy="20" r="19" fill="var(--play-bg)" stroke="#fff" stroke-width="2"/><path d="M16 13 L27 20 L16 27 Z" fill="#fff"/></svg>
      </div>
      <h4>Lorem ipsum is simply dummy text of the printing</h4>
    </div>
    <div class="video">
      <div class="video-media v3" role="img" aria-label="Video still of printed garments on display">
        <svg class="play" viewBox="0 0 40 40"><circle cx="20" cy="20" r="19" fill="var(--play-bg)" stroke="#fff" stroke-width="2"/><path d="M16 13 L27 20 L16 27 Z" fill="#fff"/></svg>
      </div>
      <h4>Lorem ipsum is simply dummy text of the printing</h4>
    </div>
  </section>
</aside>

<section class="band">
  <div class="band-inner">
    <svg width="30" height="26" viewBox="0 0 30 26"><path d="M1 12 L29 1 L23 25 L14 17 L24 6 L11 15 Z" fill="none" stroke="#fff" stroke-width="2" stroke-linejoin="round"/></svg>
    <p>Subscribe to receive updates and exclusive offers.</p>
    <div class="band-form"><div class="input">Enter your email address</div><a class="go" href="#">Subscribe</a></div>
  </div>
</section>

<footer class="footer">
  <div class="foot-cols">
    <div>
      <h5>Information</h5>
      <ul><li>Discounts</li><li>Start a Web Store / Fundraiser</li><li>Shipping</li><li>Returns</li><li>Guarantee</li><li>Terms and Conditions</li><li>Privacy</li><li>Sitemap</li></ul>
    </div>
    <div>
      <h5>About</h5>
      <ul><li>Who we are</li><li>What we do</li><li>FAQ</li><li>Blog</li></ul>
    </div>
    <div>
      <h5>Get in Touch</h5>
      <ul><li>Contact Us</li><li>Get a Quote</li><li>Online Price Check</li><li>1300 555 010</li><li>hello@loomvane.example</li></ul>
    </div>
    <div>
      <h5>Connect with Us</h5>
      <div class="socials"><span></span><span></span><span></span><span></span><span></span><span></span></div>
    </div>
  </div>
</footer>
<div class="legal">
  <div class="legal-inner">
    <span>We accept secure payment</span>
    <div class="cards"><span></span><span></span><span></span></div>
    <span class="copy">© Loom Vane. All rights reserved.</span>
  </div>
</div>

</body>
</html>
```